Flyer-Design für Sabine Wellrath Coaching für Führungskräfte
Zielgruppe
Coaching für Führungskräfte, Seminare für Führungskräfte.
Zielgruppe: Führungskräfte, Unternehmer, Geschäftsführer, Vorstände
Aufgabenstellung
Mein Logo soll beibehalten werden. Es soll ein vierseitiger Flyer sein, der meine Leistungen beschreibt. Es soll sehr modern sein (Stichwort: digital leadership) und seriös. Möglichst nicht das übliche Format, aber nicht zu groß.
Der Text soll weitgehend aus meiner Homepage (www.coaching-wellrath-beispiel.de) übernommen werden, aber es sollen auch zusätzlich Seminare aufgeführt werden.
Bis auf das Logo müssen die angehängten Dateien nicht unbedingt verwendet werden.

```html
<!DOCTYPE html>
<html lang="de">
<head>
<meta charset="utf-8">
<title>Flyer – Sabine Wellrath Coaching</title>
<link href="https://fonts.googleapis.com/css2?family=Open+Sans:ital,wght@0,400;0,600;0,700;1,700&display=swap" rel="stylesheet">
<style>
:root{
  --magenta:#d2005c;
  --navy:#164b7d;
  --ink:#3a3a3a;
  --frame:#111;
  --paper:#fff;
  --banner-dark:#0a2744;
  --banner-light:#2d6d9c;
}
html,body{margin:0;padding:0;width:1080px;height:1200px;overflow:hidden;background:#fff;}
.canvas{position:relative;width:1080px;height:1200px;overflow:hidden;}
.stage{position:absolute;left:0;top:0;width:1180px;height:1300px;transform:scale(.915);transform-origin:0 0;font-family:"Open Sans",Arial,sans-serif;color:var(--ink);}
.brief-title{position:absolute;left:28px;top:16px;font-family:Arial,Helvetica,sans-serif;font-size:22px;color:#111;margin:0;font-weight:400;}
.spread{position:absolute;left:28px;width:1116px;height:557px;border:2px solid var(--frame);background:var(--paper);box-shadow:7px 7px 7px rgba(0,0,0,.45);overflow:hidden;}
.spread--outside{top:85px;}
.spread--inside{top:715px;}
.art{position:absolute;left:0;top:0;}
.block{position:absolute;font-size:10.5px;line-height:20px;}
.block p{margin:0 0 20px;text-align:justify;hyphens:auto;-webkit-hyphens:auto;}
.block p:last-child{margin-bottom:0;}
.head{font-weight:700;font-style:italic;color:var(--magenta);font-size:12.5px;line-height:20px;margin:0;}
.claim{font-weight:700;font-style:italic;color:var(--magenta);font-size:12.5px;line-height:20px;margin:0;}
.block p.claim{text-align:left;}
.arrow-list{list-style:none;margin:0;padding:0;}
.arrow-list li{position:relative;padding-left:14px;}
.arrow-list li::before{content:"➔";position:absolute;left:0;top:0;color:var(--magenta);font-size:10px;}
.seminars li{font-weight:700;}
.block p.small{font-size:9.5px;line-height:15px;margin:0;text-align:left;}
.block p.contact{font-size:10.5px;line-height:15px;margin:0;white-space:nowrap;text-align:left;}
.brand{display:flex;align-items:center;gap:8px;color:var(--navy);font-size:10.5px;line-height:14px;font-weight:600;}
.brand .dot{width:14px;height:14px;border-radius:50%;background:var(--magenta);flex:none;}
.brand--large{font-size:14px;line-height:17px;gap:12px;}
.brand--large .dot{width:22px;height:22px;}
.quote{position:absolute;left:34px;top:28px;color:#fff;font-weight:700;font-style:italic;font-size:13.5px;line-height:19px;margin:0;}
.quote-author{position:absolute;left:34px;top:82px;color:#fff;font-size:9.5px;margin:0;}
.themes li{font-weight:700;}
.themes li span{display:block;font-weight:400;}
.core li{font-weight:700;margin-bottom:20px;}
</style>
</head>
<body>
<div class="canvas">
<div class="stage">
  <h1 class="brief-title">4-seitiger Flyer, quadraisches Format, geschlossen 148x148 mm +2 mm Beschnitt</h1>

  <section class="spread spread--outside">
    <svg class="art" width="1116" height="557" viewBox="28 85 1116 557">
      <defs>
        <linearGradient id="g-cheer" x1="0" y1="0" x2="1" y2="1">
          <stop offset="0" stop-color="#7d838b"/><stop offset="1" stop-color="#c8cbcf"/>
        </linearGradient>
        <linearGradient id="g-meeting" x1="0" y1="0" x2="1" y2="1">
          <stop offset="0" stop-color="#e6eaed"/><stop offset=".5" stop-color="#b9bec3"/><stop offset="1" stop-color="#d9dcdf"/>
        </linearGradient>
      </defs>
      <rect x="47" y="104" width="540" height="196" fill="url(#g-cheer)" role="img" aria-label="Foto: jubelnder Mann mit erhobenen Fäusten"/>
      <path d="M47,248 Q320,228 587,292 L587,302 L47,302 Z" fill="#fff"/>
      <rect x="587" y="104" width="540" height="427" fill="url(#g-meeting)" role="img" aria-label="Foto: Team in einer Besprechung am Konferenztisch"/>
      <path d="M586,532 L586,531 Q857,455 1128,531 L1128,532 Z" fill="#fff"/>
      <g>
        <circle cx="111" cy="275" r="30" fill="var(--magenta)"/>
        <path d="M97,270 h7 v18 h-7z M106,270 l6,-12 q4,-2 4,4 l-2,6 h9 q4,1 3,5 l-3,11 q-1,4 -5,4 h-12z" fill="none" stroke="#fff" stroke-width="2" stroke-linejoin="round"/>
        <circle cx="211" cy="252" r="30" fill="var(--magenta)"/>
        <path d="M211,230 l6,15 16,1 -12,10 4,16 -14,-9 -14,9 4,-16 -12,-10 16,-1z" fill="none" stroke="#fff" stroke-width="2.2" stroke-linejoin="round"/>
      </g>
    </svg>

    <div class="block" style="left:17px;top:233px;width:250px;">
      <h2 class="head">Herausforderungen annehmen</h2>
      <p>Wer eine Führungsposition einnimmt, ist gefordert: Es gilt, mit Souveränität, Kompetenz, Offenheit und auch Agilität den derzeitigen Anforderungen gerecht zu werden.</p>
      <p>Eine wertschätzende und motivierende Führung der Mitarbeiter ist für jeden erlernbar. Auch Top-Managern wurde die professionelle Mitarbeiter&shy;führung nicht geschenkt – sie ist durch eigene, kontinuierliche Weiterbildung mit der Zeit ent&shy;standen und entwickelt worden.</p>
      <p class="claim">Coaching für Führungskräfte auch<br>per Videocall oder Online-Meeting!</p>
    </div>

    <div class="block" style="left:309px;top:173px;width:240px;">
      <h2 class="head">Seminarangebote</h2>
      <ul class="arrow-list seminars">
        <li>Moderne Führung</li>
        <li>Change-Management</li>
        <li>Konfliktmanagement</li>
        <li>Zeitmanagement</li>
      </ul>
      <p class="claim" style="font-style:normal;font-size:11px;margin:6px 0 6px;">Auch als Webinare buchbar!</p>
      <p class="small">Für weiter Informationen schreiben Sie mir<br>per Mail oder rufen Sie mich direkt an!<br>Gerne können wir Termine vereinbaren,<br>ich freue mich auf Sie!</p>
      <div class="brand" style="margin:46px 0 8px;"><span class="dot"></span><span>Sabine Wellrath<br>Coaching für Führungskräfte</span></div>
      <p class="contact">Am Uferweg 21<br>41460 Musterstadt</p>
      <p class="contact" style="margin-top:13px;">Mobil: <b>0151 98765432</b><br>E-Mail: kontakt@coaching-wellrath-beispiel.de<br>http://www.coaching-wellrath-beispiel.de</p>
    </div>

    <div class="brand brand--large" style="position:absolute;left:700px;top:464px;">
      <span class="dot"></span><span>Sabine Wellrath<br>Coaching für Führungskräfte</span>
    </div>
  </section>

  <section class="spread spread--inside">
    <svg class="art" width="1116" height="557" viewBox="28 715 1116 557">
      <defs>
        <radialGradient id="g-banner" cx=".5" cy=".4" r=".8">
          <stop offset="0" stop-color="var(--banner-light)"/><stop offset="1" stop-color="var(--banner-dark)"/>
        </radialGradient>
        <linearGradient id="g-portrait" x1="0" y1="0" x2="0" y2="1">
          <stop offset="0" stop-color="#d9d2c8"/><stop offset="1" stop-color="#8d8a88"/>
        </linearGradient>
      </defs>
      <rect x="47" y="734" width="1080" height="212" fill="url(#g-banner)" role="img" aria-label="Bild: blauer Lichthintergrund mit Papierflieger, Hand und Schriftzug zur persönlichen Entwicklung"/>
      <path d="M47,946 C250,905 430,878 587,882 C760,887 950,920 1127,946 L1127,948 L47,948 Z" fill="#fff"/>
      <circle cx="402" cy="918" r="69" fill="#fff"/>
      <circle cx="402" cy="918" r="64" fill="url(#g-portrait)" role="img" aria-label="Porträtfoto der Trainerin"/>
      <g fill="none" stroke="#fff" stroke-width="2.2" stroke-linejoin="round" stroke-linecap="round">
        <circle cx="536" cy="884" r="30" fill="var(--magenta)" stroke="none"/>
        <path d="M520,876 h18 a4 4 0 0 1 4 4 v7 a4 4 0 0 1 -4 4 h-10 l-6 5 v-5 h-2 a4 4 0 0 1 -4 -4 v-7 a4 4 0 0 1 4 -4z" fill="#fff"/>
        <path d="M544,872 h8 a4 4 0 0 1 4 4 v7 a4 4 0 0 1 -4 4 v4 l-5 -4"/>
        <circle cx="641" cy="883" r="30" fill="var(--magenta)" stroke="none"/>
        <circle cx="644" cy="878" r="12"/><path d="M636,888 l-10,12"/>
        <circle cx="644" cy="874" r="3.5" fill="#fff"/><path d="M637,884 q7,-7 14,0"/>
        <circle cx="733" cy="890" r="30" fill="var(--magenta)" stroke="none"/>
        <path d="M738,870 l-12,22 h8 l-4,18 12,-24 h-8z" fill="#fff" stroke="none"/>
        <circle cx="822" cy="912" r="30" fill="var(--magenta)" stroke="none"/>
        <path d="M810,900 l18,-4 5,22 -18,4z M815,895 l14,-3"/><path d="M822,904 v10 M819,906 l3,-2"/>
        <circle cx="910" cy="938" r="30" fill="var(--magenta)" stroke="none"/>
        <circle cx="910" cy="938" r="15"/><circle cx="910" cy="938" r="8"/><circle cx="910" cy="938" r="2" fill="#fff"/><path d="M910,938 l14,-14"/>
        <circle cx="1001" cy="962" r="30" fill="var(--magenta)" stroke="none"/>
        <path d="M1014,948 q-14,0 -22,16 l6,6 q16,-8 16,-22z M992,964 l-6,1 -3,5 9,-1 M998,970 l-1,6 5,-3 1,-9 M989,973 l-5,5"/>
      </g>
    </svg>

    <p class="quote">„Wessen wir am meisten im Leben bedürfen ist jemand,<br>der uns dazu bringt, das zu tun, wozu wir fähig sind.“</p>
    <p class="quote-author">Ralf W. Ehrmann</p>

    <div class="block" style="left:17px;top:237px;width:250px;">
      <h2 class="head" style="margin-bottom:20px;">Was ich als Coach für Sie tun kann</h2>
      <p>Idealerweise verfügt eine Führungskraft über ein gesundes Selbstbewusstsein und einen eigenen Führungsstil, der durch Kompetenz gekennzeich&shy;net und damit relativ mühelos ist.</p>
      <p>Führungskräfte Coaching ist eines der wirkungs&shy;vollsten Elemente, um eine gute Unternehmens&shy;führung zu ermöglichen. Der Schwerpunkt in meinem Coaching liegt auf einer ergebnis- und lösungsorientierten Beratung. Ziel ist es, die Lern- und Leistungsfähigkeit zu verbessern. So profitiert das Unternehmen von der qualifizierteren Führungs&shy;kraft, sowie der Klient als Privatperson.</p>
    </div>

    <div class="block" style="left:286px;top:277px;width:250px;">
      <h2 class="head" style="margin-bottom:20px;">Die Kerngebiete meines Coachings</h2>
      <ul class="arrow-list core">
        <li>Die Förderung der Selbstreflexion und Wahrnehmung des Klienten.</li>
        <li>Die selbstgesteuerte Erweiterung und Ver&shy;besserung der Möglichkeiten des Klienten, sowohl in seiner Wahrnehmung, im Erleben, als auch im Verhalten.</li>
      </ul>
      <p>Voraussetzung für gelungenes Coaching ist die wertschätzende und wohlwollende Grundhaltung des Coaches und die Motivation des Klienten.</p>
    </div>

    <div class="block" style="left:580px;top:217px;width:252px;">
      <h2 class="head">Coachingthemen</h2>
      <ul class="arrow-list themes">
        <li>Entwicklung von Führungskompetenz<span>Finden Sie Ihren eigenen Führungsstil, lernen Sie souverän und erfolgreich zu führen, erwer&shy;ben Sie sich die gewünschte Anerkennung.</span></li>
        <li>Persönlichkeits- und Potentialentwicklung<span>Gestalten Sie Ihre Entwicklung aktiv, denn in je dem Menschen steckt alles Nötige, um ein glückliches und erfolgreiches Leben zu führen.</span></li>
        <li>Konfliktmanagement<span>Erweitern und verbessern Sie Ihre Möglichkeiten mit Konflikten umzugehen, lernen Sie interperso&shy;nelle und interkulturelle Differenzen kennen.</span></li>
        <li>Selbst- und Zeitmanagement<span>Verbessern Sie Ihre Leistungsfähigkeit ohne in Gefahr von Burnout zu geraten.</span></li>
      </ul>
    </div>

    <div class="block" style="left:851px;top:297px;width:246px;">
      <h2 class="head">Gesunde Führung gewinnt</h2>
      <p>Der Führungsstil hat einen erheblichen Einfluss auf den Erfolg einer Organisation. Gut geführte Mitarbeiter sind in der Regel zufrieden, motiviert und engagiert. Dies wirkt sich wiederum positiv auf die Kundenzufriedenheit aus und Sie errei&shy;chen Ihre gewünschten Ziele.</p>
      <p>Durch mein Coaching verfügen Sie über ausrei&shy;chende Kenntnisse, um professionell zu führen.</p>
    </div>
  </section>
</div>
</div>
</body>
</html>
```